Internal Office Slogans / Motto / Vision Statements

Hi. We would like to put up some posters around the office with quotations such as -
-”Do what you do so well that they will want to see it again and bring their friends.”- Hollis Trevane
-Make your customers feel heard and understood. Make your customers feel respected and liked. Make your customers feel appreciated and helped. Understand that you can do none of these things unless you are sincere about them.
Gregory Pilcott
- It’s a very predictable and satisfying phenomenon: whenever we get better, our customers do too.
Ray Casso
-Catch people in the act of performing extraordinary customer service. Treat them like heroes. Tell their stories, far and wide.
Tod Brinkerley

The purpose of the posters is to reiterate our culture and vision within the organisation. They should be clean, crisp and eye catching, not gaudy or bright. Professional, bold and strong.

The company website and logo is at http://www.nexolux.com.au
Print size will be A1

Thanks for participating & looking forward to seeing your great work.
Updates

Hi All. . 

So to reiterate we are looking for one background design to be used for multiple quotes...  The list of quotes are as follows: 

Support and or Sales Office

 

Make your customers feel heard and understood.Make your customers feel respected and liked. Make your customers feelappreciated and helped. Understand that you can do none of these things unlessyou are sincere about them.

Gregory Pilcott

 

Nothing liberates our greatness like the desireto help, the desire to serve

Rosalind Penhallow

 

It’s a very predictable and satisfying phenomenon:whenever we get better, our customers do too.

Ray Casso

 

Success means we go to sleep at night knowingthat our talents and abilities were used in a way that served others.

Rosalind Penhallow.

 

The sole purpose of business is to create, serveand satisfy a customer, from beginning to end – and that’s everyone’s job.

Tod Brinkerley

 

We don’t celebrate closing a sale, we celebrateopening a relationship.

Gwendolyn Asque

I will never make you a promise – unless I giveyou a plan and procedure to make that promise possible.

Bo Tarrick

 

Customers feel we take them for granted; onlyshow interest when we want an order; lavish our time on prospects; communicatemainly by invoice; are fixated on big accounts; drop them like hot potatoesonce we have the order; don’t follow through on promises; and satisfy our ownbureaucracy rather than their needs. We can do better than that, much better.

Peter L Osmund.

 

 

General and public area

 

Catch people in the act of performingextraordinary customer service. Treat them like heroes. Tell their stories, farand wide.

Tod Brinkerley

 

 

We see our customers as invited guests to aparty, and we are the hosts. It’s our job every day to make every importantaspect of the customer experience a little bit better." Carl Ingvold - Founder andCEO of Veltrix

 

"If you do build a great experience,customers tell each other about that. Word of mouth is verypowerful."  Carl Ingvold

 

It's not a faithin technology. It's faith in people. Neil Corrby

 

“Being the richest man in the cemetery doesn’tmatter to me … Going to bed at night saying we’ve done something wonderful…that’s what matters to me.” Neil Corrby

 

The customer experience is the next competitivebattleground. Lance Merriwether, CIO, Quorra Computers

 

”Do what you do so well that they will want tosee it again and bring their friends.”- Hollis Trevane

In the world of internet customer service, it isimportant to remember your competitor is only a mouse click away. GlenTrasky (not sure who he is but like the quote).

The customer is why you go to work. If they goaway, you do, too. Martin Glossop (?)

 

MaybeSome for Sales or Build Team:

Quality is remembered long after the price is forgotten. Varenne Family Slogan

```html
<!DOCTYPE html>
<html lang="en">
<head>
<meta charset="utf-8">
<title>Nexolux – Customer Experience Poster</title>
<link rel="stylesheet" href="https://fonts.googleapis.com/css2?family=Arimo:ital,wght@0,400;0,700;1,400&display=swap">
<style>
  :root {
    --bg-deep: #141d25;
    --bg-mid: #1f2c37;
    --bg-light: #2c3a45;
    --accent-red: #cc0000;
    --text-white: #ffffff;
    --text-muted: #9aa3aa;
  }
  * { margin: 0; padding: 0; box-sizing: border-box; }
  html, body {
    width: 848px;
    height: 1200px;
    overflow: hidden;
    background: var(--bg-deep);
  }
  .poster {
    position: relative;
    width: 848px;
    height: 1200px;
    overflow: hidden;
    font-family: "Arimo", Arial, sans-serif;
    background:
      radial-gradient(ellipse at 30% 20%, var(--bg-light) 0%, transparent 55%),
      radial-gradient(ellipse at 75% 70%, var(--bg-mid) 0%, transparent 60%),
      radial-gradient(ellipse at 50% 100%, var(--bg-mid) 0%, transparent 50%),
      var(--bg-deep);
  }
  .brand-name {
    position: absolute;
    left: 64px;
    top: 54px;
    color: var(--text-white);
    font-weight: 700;
    font-size: 46px;
    line-height: 1;
    letter-spacing: -1px;
  }
  .quote-mark {
    position: absolute;
    fill: var(--accent-red);
  }
  .quote-mark--open { left: 64px; top: 249px; width: 232px; height: 184px; }
  .quote-mark--close { left: 566px; top: 814px; width: 230px; height: 183px; }
  .quote-text {
    position: absolute;
    left: 119px;
    top: 326px;
    width: 720px;
    color: var(--text-white);
    font-weight: 700;
    font-size: 58px;
    line-height: 70.7px;
    letter-spacing: 0.3px;
  }
  .attribution {
    position: absolute;
    left: 529px;
    top: 933px;
    color: var(--text-muted);
    font-style: italic;
    font-size: 12px;
    line-height: 15px;
  }
</style>
</head>
<body>
  <main class="poster">
    <header>
      <span class="brand-name">Nexolux</span>
    </header>

    <svg class="quote-mark quote-mark--open" viewBox="0 0 236 188" preserveAspectRatio="none" aria-hidden="true">
      <path d="M0 188 V104 C0 50 20 14 58 0 L80 14 C62 28 54 50 54 78 H100 V188 Z"/>
      <path d="M136 188 V104 C136 50 156 14 194 0 L216 14 C198 28 190 50 190 78 H236 V188 Z"/>
    </svg>

    <svg class="quote-mark quote-mark--close" viewBox="0 0 234 186" preserveAspectRatio="none" aria-hidden="true">
      <path d="M100 0 V84 C100 138 80 172 42 186 L20 172 C38 158 46 136 46 108 H0 V0 Z"/>
      <path d="M234 0 V84 C234 138 214 172 176 186 L154 172 C172 158 180 136 180 108 H134 V0 Z"/>
    </svg>

    <p class="quote-text">We see our customers<br>as invited guests to<br>aparty, and we are the<br>hosts. It’s our job<br>every day to make<br>every importantaspect<br>of the customer<br>experience a little bit<br>better.</p>

    <p class="attribution">Carl Ingvold<br>Founder and CEO of Veltrix</p>
  </main>
</body>
</html>
```